Redesign of existing business card

I would like the "signage" attachment converted into a business card. This needs to be double sided aswell, keeping the phone number and names on the front, and the email + website on the back.

Second attachment is the current business card design.

Larger font for contact details is required.

Must keep to original color themes (electric blue, silver/grey etc)

Back of the card to have blue background with white writing.

Industry/Entity Type

Business

Contact Information for Business Card

Refer to existing design from attachments

Requirements
Must have
• Refer to existing design from attachments
Nice to have

```html
<!DOCTYPE html>
<html lang="en">
<head>
<meta charset="utf-8">
<title>Voltline Electrical – Business Card</title>
<link rel="stylesheet" href="https://fonts.googleapis.com/css2?family=Questrial&display=swap">
<style>
  :root {
    --electric-blue: #3d43a0;
    --electric-blue-soft: #4a50ab;
    --silver: #b9b9bd;
    --silver-light: #dcdcdf;
    --ink-grey: #6b6b70;
    --paper: #ffffff;
    --backdrop: #eceae6;
  }
  * { margin: 0; padding: 0; box-sizing: border-box; }
  html, body {
    width: 1200px; height: 818px; overflow: hidden;
    background: var(--backdrop);
    font-family: "Questrial", sans-serif;
  }
  .canvas {
    position: relative; width: 1200px; height: 818px;
    display: flex; align-items: center; justify-content: center; gap: 40px;
  }
  .card {
    position: relative; width: 540px; height: 309px; overflow: hidden;
    box-shadow: 0 6px 18px rgba(0,0,0,.18);
  }

  /* Back side */
  .card--back { background: var(--electric-blue); color: var(--paper); }
  .card--back .watermark-circle {
    position: absolute; left: 230px; top: 60px; width: 230px; height: 230px;
    border-radius: 50%; background: var(--electric-blue-soft);
  }
  .card--back .brand {
    position: absolute; left: 0; right: 0; top: 108px; text-align: center;
    color: var(--paper);
  }
  .brand__name { font-size: 42px; letter-spacing: 1px; line-height: 1; }
  .brand__tag { font-size: 15px; letter-spacing: 2px; margin-top: 6px; }
  .back-contacts {
    position: absolute; left: 26px; right: 26px; bottom: 26px;
    display: flex; align-items: center; gap: 10px; font-size: 16px;
  }
  .back-contacts .divider { opacity: .8; }
  .icon { width: 16px; height: 16px; flex: none; }

  /* Front side */
  .card--front { background: var(--paper); }
  .card--front .brand {
    position: absolute; left: 170px; top: 26px; color: var(--electric-blue);
  }
  .card--front .brand__tag { font-size: 13px; }
  .emblem-area {
    position: absolute; right: -60px; bottom: -70px; width: 330px; height: 330px;
    border-radius: 50%;
    background: radial-gradient(circle at 40% 40%, var(--silver-light), var(--silver));
  }
  .person { position: absolute; left: 26px; top: 118px; }
  .person__name { font-size: 28px; color: var(--ink-grey); }
  .person__role { font-size: 14px; color: var(--electric-blue); margin-top: 2px; letter-spacing: .5px; }
  .phone-tab {
    position: absolute; left: 0; top: 190px; height: 44px; width: 300px;
    background: var(--electric-blue); color: var(--paper);
    clip-path: polygon(0 0, 92% 0, 100% 100%, 0 100%);
    display: flex; align-items: center; gap: 10px; padding-left: 26px;
    font-size: 24px; letter-spacing: 1px;
  }
  .phone-tab .icon { width: 18px; height: 18px; }
</style>
</head>
<body>
<main class="canvas">

  <section class="card card--back" aria-label="Card back">
    <div class="watermark-circle"></div>
    <div class="brand">
      <div class="brand__name">VOLTLINE</div>
      <div class="brand__tag">ELECTRICAL</div>
    </div>
    <div class="back-contacts">
      <svg class="icon" viewBox="0 0 16 16" aria-hidden="true"><rect x="1" y="3" width="14" height="10" rx="1" fill="none" stroke="#fff" stroke-width="1.5"/><path d="M1.5 4l6.5 5 6.5-5" fill="none" stroke="#fff" stroke-width="1.5"/></svg>
      <span>daniel@voltline.com</span>
      <span class="divider">|</span>
      <svg class="icon" viewBox="0 0 16 16" aria-hidden="true"><circle cx="8" cy="8" r="6.5" fill="none" stroke="#fff" stroke-width="1.5"/><path d="M1.5 8h13M8 1.5c-3 3.5-3 9.5 0 13M8 1.5c3 3.5 3 9.5 0 13" fill="none" stroke="#fff" stroke-width="1.2"/></svg>
      <span>www.voltline.com.au</span>
    </div>
  </section>

  <section class="card card--front" aria-label="Card front">
    <div class="emblem-area" role="img" aria-label="Large silver company emblem area"></div>
    <div class="brand">
      <div class="brand__name">VOLTLINE</div>
      <div class="brand__tag">ELECTRICAL</div>
    </div>
    <div class="person">
      <div class="person__name">Daniel Reyes</div>
      <div class="person__role">Director | EC20461</div>
    </div>
    <div class="phone-tab">
      <svg class="icon" viewBox="0 0 16 16" aria-hidden="true"><path d="M4 1.5l2.5 3-1.5 1.8c.8 1.8 2 3 3.8 3.8L10.6 8.6l3 2.5-1.3 2.7C7 13.3 2.7 9 2.3 3z" fill="#fff"/></svg>
      <span>Tel 0400 555 123</span>
    </div>
  </section>

</main>
</body>
</html>
```